Australian based company requires brochure design for new safety product.

New company with no Logo or branding - Let your imagination run wild.

Marrowby Pty Ltd need a brochure designed for marketing a safety product.
The idea of the brochure is to leave with Procurement departments of the health and safety industry for quick easy reference of product specifications and benefits.

Target Market(s)

Procurement teams of Health and Safety Industry. Quick easy reference points of specifications and benefits of product.

Industry/Entity Type

Marketing

Requirements
Must have
• Must have product details and specifications as per below, preferred format A4 sheet, front to back, with attached 6 photos, as well JPEG drawing attached.

With Government legislation a requirement all electrical cords be elevated a minimum of 2 meters on construction sites - THE TORVEX STAND was developed.
With over thirty years experience in the construction industry and safety requirements that continue to evolve we have designed and developed a lead stand that is ergonomic, portable and versatile. With no other product like it on the market.

BENEFITS
- Unique portable and easy to assemble Torvexpol to fit in most tool boxes
- Non-conductive and highly visible
- Indoor and outdoor use
- Leads the way in working safely
- Complies with Government legislation
- Construction sites, Outdoor events and Camping grounds

FUNCTIONS
- Fully adjustable Telescopic Torvexpol from 1.2 meters to 4.2 meters
- Spring loaded to lock between two surfaces
- Supports multiple leads, including temporary lighting and can also be used for Laser levels
- Can be screwed to a wall to elevate above floor finishes

For all enquires please contact marrowby@fernomail.com or Dorith Pymble 0438905126

```html
<!DOCTYPE html>
<html lang="en">
<head>
<meta charset="utf-8">
<title>The Torvex Stand – Marrowby Pty Ltd</title>
<link rel="stylesheet" href="https://fonts.googleapis.com/css2?family=Archivo+Black&family=Roboto+Condensed:wght@700&family=Roboto:ital,wght@0,400;0,700;1,400&family=Poiret+One&display=swap">
<style>
  :root{
    --ink:#1e1e1e;
    --sky-top:#b9cde0;
    --sky-low:#e6edf3;
    --suit:#2b2f38;
    --brown:#4a3a30;
    --lime:#9cc62e;
    --aqua:#8fd0ea;
    --grey-hi:#f4f4f4;
    --grey-lo:#b9b9b9;
    --panel:rgba(150,150,150,.28);
    --blue-box:#1b5382;
    --green-box:#1b7a3c;
    --tab-red:#d8262c;
    --white:#ffffff;
  }
  *{margin:0;padding:0;box-sizing:border-box}
  html,body{width:848px;height:1200px;overflow:hidden}
  body{background:var(--white);font-family:"Roboto",Arial,sans-serif;color:var(--ink)}
  .brochure{position:relative;width:848px;height:1200px;overflow:hidden;
    background:linear-gradient(90deg,var(--grey-hi) 0%,#e0e0e0 40%,var(--grey-lo) 100%)}
  .hero-photo{position:absolute;left:0;top:0;width:848px;height:520px;
    background:radial-gradient(ellipse at 75% 55%,#4b4f58 0%,#3a3d45 18%,transparent 40%),
               linear-gradient(180deg,var(--sky-top) 0%,var(--sky-low) 70%,#d8d2c6 100%)}
  .title{position:absolute;left:34px;top:34px;font-family:"Archivo Black",Arial,sans-serif;
    font-size:64px;line-height:1;letter-spacing:1px;color:var(--ink)}
  .title-sub{position:absolute;left:226px;top:104px;font-family:"Poiret One",sans-serif;
    font-size:48px;letter-spacing:4px;color:var(--ink)}
  .tagline{position:absolute;left:60px;top:244px;font-family:"Roboto Condensed",Arial,sans-serif;
    font-weight:700;font-size:40px;line-height:50px;color:var(--ink)}
  .waves{position:absolute;left:0;top:390px;width:848px;height:160px}
  .intro-panel{position:absolute;left:28px;top:558px;width:792px;height:274px;background:var(--panel)}
  .intro{position:absolute;left:50px;top:570px;width:760px;font-style:italic;font-size:16.4px;line-height:21px;color:#222}
  .intro p+p{margin-top:4px}
  .product-drawing{position:absolute;left:60px;top:706px;width:730px;height:104px;
    background:linear-gradient(180deg,transparent 0%,rgba(40,140,70,.35) 25%,rgba(40,140,70,.35) 40%,rgba(90,90,90,.25) 70%,transparent 100%);
    border-radius:6px}
  .info-box{position:absolute;top:850px;height:214px;border-radius:16px;color:var(--white);
    box-shadow:4px 6px 8px rgba(0,0,0,.25)}
  .info-box.benefits{left:30px;width:386px;background:var(--blue-box)}
  .info-box.functions{left:432px;width:388px;background:var(--green-box)}
  .info-tab{position:absolute;top:-6px;left:30px;background:var(--tab-red);color:var(--white);
    font-family:"Roboto Condensed",Arial,sans-serif;font-weight:700;font-size:17px;letter-spacing:1.5px;
    padding:4px 14px 3px;border-radius:3px}
  .info-list{list-style:none;position:absolute;left:32px;top:36px;right:20px;font-style:italic;font-size:13.6px;line-height:18px}
  .info-list li{position:relative;padding-left:24px;margin-bottom:4px}
  .info-list li::before{content:"";position:absolute;left:0;top:5px;width:7px;height:7px;border-radius:50%;background:var(--white)}
  .contact{position:absolute;left:0;width:848px;text-align:center;color:var(--ink)}
  .contact.email{top:1094px;font-size:28px}
  .contact.call{top:1134px;font-size:32px;font-weight:700}
  .contact.call .label{margin-right:22px}
</style>
</head>
<body>
<main class="brochure">
  <div class="hero-photo" role="img" aria-label="Photo of two engineers in hard hats and suits on a construction site with cranes, one pointing upward and holding plans"></div>

  <h1 class="title">THE TORVEX</h1>
  <div class="title-sub">STAND</div>

  <div class="tagline">Ergonomic<br>Portable<br>Versatile</div>

  <svg class="waves" viewBox="0 0 848 160" preserveAspectRatio="none" aria-hidden="true">
    <path d="M0 60 C220 90 420 130 600 110 C720 95 800 50 848 20 L848 160 L0 160 Z" fill="var(--aqua)"/>
    <path d="M0 72 C220 100 420 138 600 118 C720 104 800 62 848 36 L848 160 L0 160 Z" fill="var(--brown)"/>
    <path d="M0 96 C220 118 440 150 620 135 C730 126 800 100 848 80 L848 160 L0 160 Z" fill="var(--lime)"/>
    <path d="M0 104 C220 126 440 158 620 143 C730 134 800 110 848 92 L848 160 L0 160 Z" fill="#ececec"/>
  </svg>

  <div class="intro-panel"></div>
  <div class="intro">
    <p>With Government legislation a requirement all electrical cords be elevated a minimum of 2 meters on construction sites - THE TORVEX STAND was developed.</p>
    <p>With over thirty years experience in the construction industry and safety requirements that continue to evolve we have designed and developed a lead stand that is ergonomic, portable and versatile. With no other product like it on the market.</p>
  </div>
  <div class="product-drawing" role="img" aria-label="Technical drawing of the green telescopic stand with yellow end plates, clamp and ground spike"></div>

  <section class="info-box benefits">
    <h2 class="info-tab">BENEFITS</h2>
    <ul class="info-list">
      <li>Unique portable and easy to assemble Torvexpol to fit in most tool boxes</li>
      <li>Non-conductive and highly visible</li>
      <li>Indoor and outdoor use</li>
      <li>Leads the way in working safely</li>
      <li>Complies with Government legislation</li>
      <li>Construction sites, Outdoor events and Camping grounds</li>
    </ul>
  </section>

  <section class="info-box functions">
    <h2 class="info-tab">FUNCTIONS</h2>
    <ul class="info-list">
      <li>Fully adjustable Telescopic Torvexpol from 1.2 meters to 4.2 meters</li>
      <li>Spring loaded to lock between two surfaces</li>
      <li>Supports multiple leads, including temporary lighting and can also be used for Laser levels</li>
      <li>Can be screwed to a wall to elevate above floor finishes</li>
    </ul>
  </section>

  <p class="contact email">email:&nbsp; marrowby@fernomail.com</p>
  <p class="contact call"><span class="label">or call</span>Dorith Pymble 0438905126</p>
</main>
</body>
</html>
```